Website Design for a holiday home letting busines

We require a redesign of our present website www.birchwoodstays.com. We want the website to stand out and look professional and clean to make holiday hunters want to book a caravan or lodge holiday with us. Our logo is red however we DO NOT want the website to be red. We want a natural colour scheme.

The final design should communicate that we are a professional company to book with.

On the home page we require;
Overview of company
Photo
Search box for holiday (check in)
Late Deals
Reviews
News

We would like the following pages designed; home page, available dates page, caravans page, content page.

The website should be responsive for smart phones. One website I do like is http://www.verdamoro.be/nl/

Target Market(s)

Families

Industry/Entity Type

Travel

Number of Pages Required

5+ page

Font styles to use
Serif

Requirements
Must have
• The project must be responsive for mobile phones and tablets.
• Ability to search for holiday home holidays
• We want a natural colour scheme.
Nice to have
• A style we like is http://www.verdamoro.be/nl/
Should not have
• Do not use red as a colour for the website. Our logo is red so this is the only time we want this used.

```html
<!DOCTYPE html>
<html lang="en">
<head>
<meta charset="utf-8">
<title>Birchwood Stays – Private Holiday Rentals</title>
<link rel="stylesheet" href="https://fonts.googleapis.com/css2?family=Open+Sans:wght@300;400;600;700;800&display=swap">
<style>
:root{
  --green:#7cbf3f;
  --green-dark:#5fa12a;
  --green-soft:#e4f1d8;
  --navy:#1f3a5c;
  --navy-dark:#162c47;
  --ink:#444a50;
  --muted:#8a9096;
  --line:#e2e4e6;
  --grey-bg:#f4f5f6;
  --foot:#3b4046;
  --foot-dark:#2c3035;
  --foot-text:#b7bcc2;
  --logo-red:#c8262c;
  --white:#fff;
}
*{box-sizing:border-box;margin:0;padding:0}
html,body{width:1200px;height:3076px;overflow:hidden}
body{font-family:"Open Sans",Arial,sans-serif;color:var(--ink);background:var(--white);font-size:13px;line-height:1.55;position:relative}
.wrap{width:960px;margin:0 auto;position:relative}
.btn{display:inline-block;background:var(--green);color:var(--white);font-weight:700;font-size:12px;text-transform:uppercase;padding:9px 18px;border-radius:2px;letter-spacing:.5px}
.section-title{text-align:center;font-weight:300;font-size:34px;color:var(--green-dark);position:relative;padding-bottom:14px;margin-bottom:34px}
.section-title::after{content:"";position:absolute;left:50%;bottom:0;width:60px;height:2px;margin-left:-30px;background:var(--green)}

/* header */
.site-header{height:100px}
.brand{position:absolute;left:0;top:22px;display:flex;align-items:center;gap:10px}
.brand-mark{width:44px;height:44px;border-radius:50%;background:var(--logo-red)}
.brand-name{font-size:28px;font-weight:700;color:var(--logo-red)}
.header-contact{position:absolute;right:0;top:20px;text-align:right;font-size:13px;color:var(--ink)}
.header-contact strong{display:block;font-size:15px;color:var(--navy)}

/* hero */
.hero{position:relative;height:420px}
.hero-photo{position:absolute;inset:0;background:linear-gradient(180deg,#7fc3ea 0%,#b9e1f4 45%,#4aa6c4 60%,#e9d8b4 78%,#d9c296 100%)}
.hero-accent{position:absolute;right:170px;top:70px;width:360px;height:340px;border-radius:50%;background:radial-gradient(circle,#f4d7c0 0%,#e8b98f 55%,rgba(232,185,143,0) 72%)}
.main-nav{position:absolute;left:120px;top:0;width:960px;height:34px;background:var(--green);display:flex}
.main-nav a{color:var(--white);font-size:12px;font-weight:600;padding:0 20px;line-height:34px;border-right:1px solid rgba(255,255,255,.25)}
.main-nav a:first-child{background:var(--green-dark)}
.hero-copy{position:absolute;left:120px;top:110px;width:420px}
.hero-copy h1{color:var(--white);font-size:38px;font-weight:800;line-height:1.1;text-transform:uppercase;text-shadow:0 1px 3px rgba(0,0,0,.25)}
.hero-copy p{color:#d9f2b8;font-size:17px;font-weight:600;line-height:1.35;margin:10px 0 26px;text-shadow:0 1px 2px rgba(0,0,0,.3)}

/* search */
.search{position:absolute;left:120px;top:508px;width:960px;height:82px;background:var(--navy);padding:14px 20px;display:flex;gap:16px;align-items:flex-end}
.search .field{flex:1}
.search label{display:block;color:var(--white);font-size:10px;font-weight:700;text-transform:uppercase;margin-bottom:5px}
.search .input{height:32px;background:var(--white);border-radius:2px;font-size:11px;color:var(--muted);padding:0 10px;line-height:32px;display:flex;justify-content:space-between;align-items:center}
.search .btn{height:32px;padding:0 30px;line-height:32px}

/* about */
.about{padding-top:110px;height:530px}
.about-body{display:flex;gap:60px}
.about-photo{width:320px;height:320px;border-radius:50%;background:radial-gradient(circle at 50% 40%,#e8dcc6,#b59a7c 70%,#8c7358);flex:none;border:6px solid var(--white);box-shadow:0 0 0 1px var(--line)}
.about-text p{margin-bottom:14px;font-size:12.5px;color:var(--muted)}

/* caravans */
.caravans{background:var(--grey-bg);height:420px;padding-top:40px}
.caravan-list{display:flex;justify-content:space-between;padding:0 30px}
.caravan{width:190px;text-align:center}
.caravan-photo{width:180px;height:180px;border-radius:50%;margin:0 auto 16px;background:radial-gradient(circle at 50% 40%,#ede3d2,#c4ab8a 70%,#927758);position:relative;overflow:hidden;border:4px solid var(--white)}
.caravan-photo .overlay{position:absolute;inset:0;background:rgba(31,58,92,.75);color:var(--white);display:flex;flex-direction:column;align-items:center;justify-content:center;font-size:17px;font-weight:600}
.caravan-photo .overlay span{font-size:12px;color:#c9ea9f;font-weight:400}
.caravan p{font-size:11.5px;color:var(--muted)}

/* late deals */
.deals{background:var(--green-soft);height:400px;padding-top:36px}
.deal-list{display:flex;gap:30px;justify-content:center}
.deal{width:450px;height:200px;display:flex;background:var(--white)}
.deal-photo{width:210px;background:linear-gradient(160deg,#e6d9c2,#b49672 60%,#7e6347)}
.deal-info{flex:1;background:var(--navy);color:var(--white);display:flex;flex-direction:column}
.deal-info h3{font-size:15px;font-weight:600;padding:12px 14px 4px;text-transform:uppercase}
.deal-info p{font-size:11px;color:#c3cfdc;padding:0 14px}
.deal-icons{display:flex;gap:12px;padding:12px 14px}
.deal-foot{margin-top:auto;display:flex;background:var(--navy-dark)}
.deal-price{flex:1;background:var(--green);font-size:17px;font-weight:700;padding:8px 14px}
.deal-foot .book{padding:10px 14px;font-size:11px;font-weight:700}
.slider-nav{display:flex;gap:10px;justify-content:center;margin-top:18px}
.slider-nav span{width:24px;height:24px;border-radius:50%;background:var(--green);display:flex;align-items:center;justify-content:center}

/* reviews & news */
.columns{height:680px;padding-top:40px;display:flex;gap:40px}
.col{flex:1}
.col-head{display:flex;justify-content:space-between;align-items:center;border-bottom:2px solid var(--green);padding-bottom:8px;margin-bottom:34px}
.col-head h2{font-size:28px;font-weight:300;color:var(--green-dark)}
.col-head a{font-size:10px;font-weight:700;color:var(--white);background:var(--green);padding:3px 8px}
.review{display:flex;gap:22px;margin-bottom:70px}
.review-photo{width:170px;height:170px;border-radius:50%;flex:none;background:radial-gradient(circle at 50% 45%,#f5ddc8,#e0ad83 55%,#b88460)}
.review h3,.news h3{font-size:13px;font-weight:700;color:var(--navy);text-transform:uppercase;margin-bottom:6px}
.review p{font-size:12.5px;color:var(--muted);margin-bottom:10px}
.review .who{font-size:12px;color:var(--green-dark);font-weight:600}
.stars{display:flex;gap:2px;align-items:center;font-size:11px;color:var(--muted)}
.news{display:flex;gap:14px;margin-bottom:18px}
.news-date{width:44px;height:44px;flex:none;background:var(--navy);color:var(--white);text-align:center;font-size:16px;font-weight:700;line-height:44px}
.news h3{text-transform:none;font-size:16px;font-weight:600;margin:0}
.news .meta{font-size:11px;color:var(--green-dark)}
.news-text{font-size:12.5px;color:var(--muted);margin-bottom:50px}

/* footer */
.site-footer{position:absolute;left:0;top:2500px;width:1200px;height:576px;background:var(--foot);color:var(--foot-text)}
.foot-top{display:flex;gap:40px;padding-top:30px;height:270px;border-bottom:1px solid #4a5057}
.foot-top h2,.foot-bottom h2{color:var(--white);font-size:22px;font-weight:600;margin-bottom:16px}
.quick-links{flex:1}
.link-cols{display:flex;gap:34px}
.link-cols ul{list-style:none;font-size:11.5px}
.link-cols li{padding:4px 0;border-bottom:1px solid #4a5057}
.link-cols li::before{content:"› ";color:var(--green)}
.gallery{width:420px}
.gallery-grid{display:grid;grid-template-columns:repeat(4,1fr);gap:14px}
.gallery-grid div{width:90px;height:90px;border-radius:50%;background:radial-gradient(circle,#e2d3bb,#a88c69 65%,#6e5740)}
.foot-bottom{display:flex;gap:40px;padding-top:24px;height:226px}
.foot-about{flex:1;font-size:11.5px}
.foot-about p{margin-bottom:8px}
.foot-contact{width:300px}
.foot-contact .input{height:28px;background:#4a5057;margin-bottom:8px;font-size:11px;padding:0 10px;line-height:28px}
.foot-contact .area{height:48px}
.foot-contact .btn{padding:7px 18px}
.foot-badge{width:200px;display:flex;flex-direction:column;align-items:center;gap:18px;padding-top:6px}
.badge-shape{width:120px;height:120px;border-radius:50%;background:var(--white);border:8px solid var(--green)}
.social{display:flex;gap:8px}
.social span{width:28px;height:28px;border-radius:3px}
.copyright{position:absolute;left:0;bottom:0;width:1200px;height:40px;background:var(--foot-dark);font-size:10.5px;line-height:40px}
</style>
</head>
<body>

<header class="site-header">
  <div class="wrap">
    <div class="brand"><span class="brand-mark"></span><span class="brand-name">Birchwood Stays</span></div>
    <div class="header-contact"><strong>01632 960 418</strong>info@birchwoodstays.com</div>
  </div>
</header>

<section class="hero">
  <div class="hero-photo" role="img" aria-label="Child on a sunny beach holding a colourful pinwheel, blue sea and sky behind"></div>
  <div class="hero-accent" role="img" aria-label="Soft warm light around the child and pinwheel"></div>
  <nav class="main-nav">
    <a>Caravans &amp; Lodges</a><a>Holidays</a><a>Payment Plans</a><a>Fernlea Castle</a><a>Local Attractions</a><a>Reviews</a><a>Contact Us</a>
  </nav>
  <div class="hero-copy">
    <h1>Private Holiday Rentals</h1>
    <p>Quality Lodge &amp; Caravan Hire at Fernlea Castle Holiday Park, Northumberland</p>
    <span class="btn">More Details</span>
  </div>
</section>

<form class="search">
  <div class="field"><label>Destination</label><div class="input">Fernlea Castle Park</div></div>
  <div class="field"><label>Check in</label><div class="input">Select date
    <svg width="12" height="12" viewBox="0 0 12 12"><rect x="1" y="2" width="10" height="9" fill="none" stroke="#8a9096"/><line x1="1" y1="5" x2="11" y2="5" stroke="#8a9096"/></svg></div></div>
  <div class="field"><label>Check out</label><div class="input">Select date
    <svg width="12" height="12" viewBox="0 0 12 12"><rect x="1" y="2" width="10" height="9" fill="none" stroke="#8a9096"/><line x1="1" y1="5" x2="11" y2="5" stroke="#8a9096"/></svg></div></div>
  <span class="btn">Book Now</span>
</form>

<section class="about">
  <div class="wrap">
    <h2 class="section-title">About Us</h2>
    <div class="about-body">
      <div class="about-photo" role="img" aria-label="Bright caravan dining area with table set and flowers"></div>
      <div class="about-text">
        <p>We are a family run business offering quality holiday homes on a peaceful park by the coast. Every lodge and caravan is privately owned, cleaned with care and checked before each stay so that you can relax from the moment you arrive.</p>
        <p>Our homes suit couples, small groups and families with young children. Many have decking, sea views and double glazing, and all are a short walk from the pools, play areas, shops and restaurants on the park.</p>
        <p>Booking is simple and secure. Choose your dates, pick the home that suits you and pay in easy stages. Our friendly team is always on hand to answer questions before and during your holiday.</p>
        <span class="btn">Book Now</span>
      </div>
    </div>
  </div>
</section>

<section class="caravans">
  <div class="wrap">
    <h2 class="section-title">Our Caravans and Lodges</h2>
    <div class="caravan-list">
      <div class="caravan"><div class="caravan-photo" role="img" aria-label="Caravan lounge interior"><div class="overlay">Willow Crest<span>£350 per week</span></div></div><p>Spacious two bedroom caravan with a bright lounge and full kitchen.</p></div>
      <div class="caravan"><div class="caravan-photo" role="img" aria-label="Caravan lounge interior"></div><p>Modern three bedroom caravan close to the park pools and shops.</p></div>
      <div class="caravan"><div class="caravan-photo" role="img" aria-label="Lodge living room interior"></div><p>Luxury lodge with decking, open plan living and calm sea views.</p></div>
      <div class="caravan"><div class="caravan-photo" role="img" aria-label="Lodge kitchen and dining interior"></div><p>Cosy family lodge with central heating and a private parking bay.</p></div>
    </div>
  </div>
</section>

<section class="deals">
  <div class="wrap">
    <h2 class="section-title">Late Deals</h2>
    <div class="deal-list">
      <article class="deal">
        <div class="deal-photo" role="img" aria-label="Caravan lounge with sofas"></div>
        <div class="deal-info">
          <h3>The Seabreeze</h3>
          <p>Three bedroom caravan for up to eight guests, close to the beach path.</p>
          <div class="deal-icons">
            <svg width="16" height="14" viewBox="0 0 16 14"><rect x="1" y="6" width="14" height="5" fill="#c3cfdc"/><rect x="1" y="3" width="5" height="3" fill="#c3cfdc"/></svg>
            <svg width="16" height="14" viewBox="0 0 16 14"><circle cx="8" cy="5" r="3" fill="#c3cfdc"/><rect x="3" y="9" width="10" height="4" rx="2" fill="#c3cfdc"/></svg>
            <svg width="16" height="14" viewBox="0 0 16 14"><rect x="2" y="2" width="12" height="8" fill="none" stroke="#c3cfdc" stroke-width="1.5"/><line x1="5" y1="13" x2="11" y2="13" stroke="#c3cfdc" stroke-width="1.5"/></svg>
          </div>
          <div class="deal-foot"><span class="deal-price">£199.00</span><span class="book">BOOK NOW</span></div>
        </div>
      </article>
      <article class="deal">
        <div class="deal-photo" role="img" aria-label="Caravan lounge with sofas"></div>
        <div class="deal-info">
          <h3>The Seabreeze</h3>
          <p>Three bedroom caravan for up to eight guests, close to the beach path.</p>
          <div class="deal-icons">
            <svg width="16" height="14" viewBox="0 0 16 14"><rect x="1" y="6" width="14" height="5" fill="#c3cfdc"/><rect x="1" y="3" width="5" height="3" fill="#c3cfdc"/></svg>
            <svg width="16" height="14" viewBox="0 0 16 14"><circle cx="8" cy="5" r="3" fill="#c3cfdc"/><rect x="3" y="9" width="10" height="4" rx="2" fill="#c3cfdc"/></svg>
            <svg width="16" height="14" viewBox="0 0 16 14"><rect x="2" y="2" width="12" height="8" fill="none" stroke="#c3cfdc" stroke-width="1.5"/><line x1="5" y1="13" x2="11" y2="13" stroke="#c3cfdc" stroke-width="1.5"/></svg>
          </div>
          <div class="deal-foot"><span class="deal-price">£199.00</span><span class="book">BOOK NOW</span></div>
        </div>
      </article>
    </div>
    <div class="slider-nav">
      <span><svg width="8" height="10" viewBox="0 0 8 10"><path d="M6 1 2 5l4 4" fill="none" stroke="#fff" stroke-width="2"/></svg></span>
      <span><svg width="8" height="10" viewBox="0 0 8 10"><path d="M2 1l4 4-4 4" fill="none" stroke="#fff" stroke-width="2"/></svg></span>
    </div>
  </div>
</section>

<section class="wrap columns">
  <div class="col">
    <div class="col-head"><h2>Reviews</h2><a>VIEW ALL</a></div>
    <div class="review">
      <div class="review-photo" role="img" aria-label="Smiling guest portrait"></div>
      <div>
        <h3>Willow Crest</h3>
        <p>A lovely clean caravan with everything we needed. The children loved the pool and we loved the quiet evenings on the deck. We will be booking again next summer without a doubt.</p>
        <div class="who">Hannah Pryor</div>
        <div class="stars">
          <svg width="60" height="11" viewBox="0 0 60 11"><g fill="#7cbf3f"><path d="M5.5 0l1.6 3.6 3.9.4-2.9 2.6.8 3.9-3.4-2-3.4 2 .8-3.9L0 4l3.9-.4z"/><path transform="translate(12)" d="M5.5 0l1.6 3.6 3.9.4-2.9 2.6.8 3.9-3.4-2-3.4 2 .8-3.9L0 4l3.9-.4z"/><path transform="translate(24)" d="M5.5 0l1.6 3.6 3.9.4-2.9 2.6.8 3.9-3.4-2-3.4 2 .8-3.9L0 4l3.9-.4z"/><path transform="translate(36)" d="M5.5 0l1.6 3.6 3.9.4-2.9 2.6.8 3.9-3.4-2-3.4 2 .8-3.9L0 4l3.9-.4z"/><path transform="translate(48)" d="M5.5 0l1.6 3.6 3.9.4-2.9 2.6.8 3.9-3.4-2-3.4 2 .8-3.9L0 4l3.9-.4z"/></g></svg>
          &nbsp;14 Reviews
        </div>
      </div>
    </div>
    <div class="review">
      <div class="review-photo" role="img" aria-label="Smiling guest portrait"></div>
      <div>
        <h3>Willow Crest</h3>
        <p>Great location and a warm welcome from the team. The caravan was spotless and spacious, and the beach walk each morning was the highlight of our family break.</p>
        <div class="who">Hannah Pryor</div>
        <div class="stars">
          <svg width="60" height="11" viewBox="0 0 60 11"><g fill="#7cbf3f"><path d="M5.5 0l1.6 3.6 3.9.4-2.9 2.6.8 3.9-3.4-2-3.4 2 .8-3.9L0 4l3.9-.4z"/><path transform="translate(12)" d="M5.5 0l1.6 3.6 3.9.4-2.9 2.6.8 3.9-3.4-2-3.4 2 .8-3.9L0 4l3.9-.4z"/><path transform="translate(24)" d="M5.5 0l1.6 3.6 3.9.4-2.9 2.6.8 3.9-3.4-2-3.4 2 .8-3.9L0 4l3.9-.4z"/><path transform="translate(36)" d="M5.5 0l1.6 3.6 3.9.4-2.9 2.6.8 3.9-3.4-2-3.4 2 .8-3.9L0 4l3.9-.4z"/><path transform="translate(48)" d="M5.5 0l1.6 3.6 3.9.4-2.9 2.6.8 3.9-3.4-2-3.4 2 .8-3.9L0 4l3.9-.4z"/></g></svg>
          &nbsp;14 Reviews
        </div>
      </div>
    </div>
  </div>
  <div class="col">
    <div class="col-head"><h2>Latest News</h2><a>VIEW ALL</a></div>
    <div class="news"><div class="news-date">12</div><div><h3>Sunny Stage Show Live At Fernlea Castle</h3><div class="meta">Posted on 12 August 2015</div></div></div>
    <p class="news-text">The popular Sunny Stage Show returns to the park theatre this summer with songs, dancing and games for all the family. Shows run every evening through the school holidays, so book your stay early to join the fun.</p>
    <div class="news"><div class="news-date">04</div><div><h3>Easter With Daniel Marsh</h3><div class="meta">Posted on 4 March 2015</div></div></div>
    <p class="news-text">Join us this Easter weekend for a live evening with singer Daniel Marsh in the main clubhouse. There will be an egg hunt for the children, face painting and a family disco, with spaces limited.</p>
  </div>
</section>

<footer class="site-footer">
  <div class="wrap">
    <div class="foot-top">
      <div class="quick-links">
        <h2>Quick Links</h2>
        <div class="link-cols">
          <ul><li>About Us</li><li>Caravans &amp; Lodges</li><li>2015 Holidays</li><li>2016 Holidays</li><li>Late Deals</li><li>Fernlea Castle</li></ul>
          <ul><li>Local Attractions</li><li>Guest Reviews</li><li>Contact Us</li><li>Payment Plans</li><li>Latest News</li><li>FAQs</li></ul>
          <ul><li>Frequently Asked Questions</li><li>Park Entertainment</li><li>Privacy Policy</li><li>Booking Terms</li></ul>
        </div>
      </div>
      <div class="gallery">
        <h2>Photo Gallery</h2>
        <div class="gallery-grid" role="img" aria-label="Gallery of caravan and lodge interior photos">
          <div></div><div></div><div></div><div></div><div></div><div></div><div></div><div></div>
        </div>
      </div>
    </div>
    <div class="foot-bottom">
      <div class="foot-about">
        <h2>Birchwood Stays</h2>
        <p>12 Fernlea Park, Unit 7<br>Fernlea Castle Holiday Park<br>Fernlea-on-Tweed, Northumberland</p>
        <p>01632 960 418<br>info@birchwoodstays.com</p>
      </div>
      <div class="foot-contact">
        <h2>Contact Us</h2>
        <div class="input">Name</div>
        <div class="input">Email</div>
        <div class="input area">Message</div>
        <span class="btn">Send</span>
      </div>
      <div class="foot-badge">
        <div class="badge-shape" role="img" aria-label="Guest rating award badge"></div>
        <div class="social">
          <span style="background:#4a76a8"></span><span style="background:#5aa9d6"></span><span style="background:#c94a4a"></span><span style="background:#6b7a8a"></span>
        </div>
      </div>
    </div>
  </div>
  <div class="copyright"><div class="wrap">© 2015 Birchwood Stays. All rights reserved. Registered in England. Holiday homes privately owned and let by Birchwood Stays at Fernlea Castle Holiday Park.</div></div>
</footer>

</body>
</html>
```